Brightwall painting and decorating *

Need a flyer design to advertise my services
So the information I need included is the services we offer at brightwall painting and decorating which include
Interior painting
Exterior painting
Wallpaper hanging
Paint and cellulose spraying
Dust free sanding
Pressure washing
Stone cleaning
Also would need to have my company contact details in
Www.brightwallpaintingdecorating.co.uk
Email is info@brightwallpaintingdecorating.com
Brightwall Painting & Decorating Services has a proven track record of innovative designs, effective problem solving and attention to detail and our goal is to meet and exceed the expectations of every customer. We take on all types of jobs from small domestic work to larger commercial projects, all carried out to the highest standards, and at very competitive prices.
Colors
Designer to choose colors to be used in the design.
Look and feel

```html
<!DOCTYPE html>
<html lang="en">
<head>
<meta charset="utf-8">
<title>Brightwall Painting and Decorating – Flyer</title>
<link rel="stylesheet" href="https://fonts.googleapis.com/css2?family=Montserrat:wght@800&family=Open+Sans:wght@600;700;800&family=Oswald:wght@600&display=swap">
<style>
  :root {
    --navy: #0f4c8a;
    --navy-deep: #0b3c70;
    --sky: #3f8fd8;
    --ring: #8fbce6;
    --ink: #1a1a1a;
    --paper: #ffffff;
    --page: #e9e9e9;
  }
  * { margin: 0; padding: 0; box-sizing: border-box; }
  html, body { width: 852px; height: 1200px; overflow: hidden; background: var(--page); }
  .flyer { position: relative; width: 852px; height: 1200px; overflow: hidden; background: var(--paper); font-family: "Open Sans", sans-serif; }
  .flyer-art { position: absolute; inset: 0; }

  .offer-title { position: absolute; left: 61px; top: 650px; font-family: "Montserrat", sans-serif; font-weight: 800; font-size: 36px; color: var(--paper); letter-spacing: 0.5px; }
  .offer-title .accent { color: var(--sky); }
  .offer-rule { position: absolute; left: 62px; top: 700px; width: 32px; height: 3px; background: var(--paper); }

  .service-list { position: absolute; left: 62px; top: 746px; list-style: none; }
  .service-list li { display: flex; align-items: center; height: 51.5px; font-weight: 700; font-size: 21px; color: var(--paper); letter-spacing: 0.3px; white-space: nowrap; }
  .tick { width: 19px; height: 19px; margin-right: 26px; flex: none; }

  .follow { position: absolute; left: 66px; top: 1140px; display: flex; align-items: center; gap: 8px; }
  .follow-label { font-weight: 700; font-size: 19px; color: var(--sky); text-decoration: underline; margin-right: 4px; }
  .social-dot { width: 26px; height: 26px; border-radius: 50%; background: var(--paper); }
  .mail-icon { width: 28px; height: 22px; }

  .brand-name { position: absolute; left: 467px; top: 672px; width: 350px; text-align: center; font-family: "Montserrat", sans-serif; font-weight: 800; font-size: 46px; line-height: 1.1; color: var(--navy); white-space: nowrap; }
  .brand-tag { position: absolute; left: 467px; top: 728px; width: 350px; text-align: center; font-weight: 700; font-size: 15px; color: var(--sky); letter-spacing: 0.3px; white-space: nowrap; }
  .brand-rule { position: absolute; top: 757px; height: 2px; background: var(--navy); }
  .brand-rule.left { left: 470px; width: 120px; }
  .brand-rule.right { left: 694px; width: 120px; }
  .brand-dot { position: absolute; left: 634px; top: 750px; width: 16px; height: 16px; border-radius: 50%; background: var(--navy); }

  .headline { position: absolute; left: 467px; top: 822px; width: 350px; text-align: center; font-family: "Oswald", sans-serif; font-weight: 600; font-size: 80px; line-height: 1; color: var(--navy); white-space: nowrap; transform: scaleX(0.8); transform-origin: center; }
  .headline-sub { position: absolute; left: 467px; top: 928px; width: 350px; text-align: center; font-weight: 700; font-size: 22px; color: var(--sky); letter-spacing: 0.5px; white-space: nowrap; }

  .contact { position: absolute; left: 473px; display: flex; align-items: center; line-height: 1; white-space: nowrap; }
  .contact svg { flex: none; }
  .contact.phone { top: 1050px; height: 40px; }
  .contact.phone .value { font-weight: 800; font-size: 36px; color: var(--ink); margin-left: 16px; letter-spacing: 0.5px; }
  .contact.email { top: 1104px; height: 20px; }
  .contact.web { top: 1137px; height: 22px; }
  .contact.email .value, .contact.web .value { font-weight: 700; font-size: 14px; color: var(--ink); margin-left: 18px; }

  .foot-bar { position: absolute; left: 643px; top: 1186px; width: 209px; height: 14px; background: var(--sky); }
</style>
</head>
<body>
<main class="flyer">
  <svg class="flyer-art" viewBox="0 0 852 1200" width="852" height="1200">
    <defs>
      <linearGradient id="roomTone" x1="0" y1="0" x2="1" y2="1">
        <stop offset="0" stop-color="#d9d9d9"/>
        <stop offset="0.45" stop-color="#f1f1f1"/>
        <stop offset="0.75" stop-color="#b9b6b2"/>
        <stop offset="1" stop-color="#7a4a2e"/>
      </linearGradient>
      <linearGradient id="studioTone" x1="0" y1="0" x2="0" y2="1">
        <stop offset="0" stop-color="#eeeeee"/>
        <stop offset="1" stop-color="#d9b98a"/>
      </linearGradient>
      <linearGradient id="loungeTone" x1="0" y1="0" x2="0" y2="1">
        <stop offset="0" stop-color="#eceae3"/>
        <stop offset="0.55" stop-color="#d8cdbd"/>
        <stop offset="1" stop-color="#c9c6c0"/>
      </linearGradient>
      <linearGradient id="panelTone" x1="0" y1="0" x2="0" y2="1">
        <stop offset="0" stop-color="#0f4c8a"/>
        <stop offset="1" stop-color="#0b3c70"/>
      </linearGradient>
    </defs>

    <rect class="hero-photo" x="0" y="0" width="852" height="720" fill="url(#roomTone)" role="img" aria-label="Photo of a bright modern open-plan living and dining room"/>

    <path class="white-sweep" d="M0,555 C220,520 520,470 852,330 L852,1200 L0,1200 Z" fill="#ffffff"/>
    <path class="navy-swoosh" d="M590,478 C690,440 780,395 852,352 L852,380 C780,425 700,470 620,500 Z" fill="#0f4c8a"/>

    <path class="panel-edge" d="M0,552 C140,540 270,560 378,612 C420,720 440,830 446,950 C450,1060 434,1140 398,1200 L0,1200 Z" fill="#3f8fd8"/>
    <path class="service-panel" d="M0,550 C130,538 255,556 360,606 C400,715 420,825 428,950 C433,1060 416,1140 380,1200 L0,1200 Z" fill="url(#panelTone)"/>

    <circle cx="666" cy="436" r="140" fill="#8fbce6"/>
    <circle class="circle-photo" cx="666" cy="436" r="128" fill="url(#loungeTone)" role="img" aria-label="Photo of a freshly decorated lounge with dining table"/>

    <circle cx="400" cy="530" r="120" fill="#8fbce6"/>
    <circle class="circle-photo" cx="400" cy="530" r="108" fill="url(#studioTone)" role="img" aria-label="Photo of a white painted work corner with easel"/>
  </svg>

  <h2 class="offer-title">WE <span class="accent">OFFER</span></h2>
  <div class="offer-rule"></div>

  <ul class="service-list">
    <li><svg class="tick" viewBox="0 0 20 20"><circle cx="10" cy="10" r="10" fill="#4d96dc"/><path d="M5.5 10.5 L8.6 13.4 L14.5 7" fill="none" stroke="#0f4c8a" stroke-width="2.4" stroke-linecap="round" stroke-linejoin="round"/></svg>Interior painting</li>
    <li><svg class="tick" viewBox="0 0 20 20"><circle cx="10" cy="10" r="10" fill="#4d96dc"/><path d="M5.5 10.5 L8.6 13.4 L14.5 7" fill="none" stroke="#0f4c8a" stroke-width="2.4" stroke-linecap="round" stroke-linejoin="round"/></svg>Exterior painting</li>
    <li><svg class="tick" viewBox="0 0 20 20"><circle cx="10" cy="10" r="10" fill="#4d96dc"/><path d="M5.5 10.5 L8.6 13.4 L14.5 7" fill="none" stroke="#0f4c8a" stroke-width="2.4" stroke-linecap="round" stroke-linejoin="round"/></svg>Wallpaper hanging</li>
    <li><svg class="tick" viewBox="0 0 20 20"><circle cx="10" cy="10" r="10" fill="#4d96dc"/><path d="M5.5 10.5 L8.6 13.4 L14.5 7" fill="none" stroke="#0f4c8a" stroke-width="2.4" stroke-linecap="round" stroke-linejoin="round"/></svg>Paint &amp; cellulose spraying</li>
    <li><svg class="tick" viewBox="0 0 20 20"><circle cx="10" cy="10" r="10" fill="#4d96dc"/><path d="M5.5 10.5 L8.6 13.4 L14.5 7" fill="none" stroke="#0f4c8a" stroke-width="2.4" stroke-linecap="round" stroke-linejoin="round"/></svg>Dust free sanding</li>
    <li><svg class="tick" viewBox="0 0 20 20"><circle cx="10" cy="10" r="10" fill="#4d96dc"/><path d="M5.5 10.5 L8.6 13.4 L14.5 7" fill="none" stroke="#0f4c8a" stroke-width="2.4" stroke-linecap="round" stroke-linejoin="round"/></svg>Pressure washing</li>
    <li><svg class="tick" viewBox="0 0 20 20"><circle cx="10" cy="10" r="10" fill="#4d96dc"/><path d="M5.5 10.5 L8.6 13.4 L14.5 7" fill="none" stroke="#0f4c8a" stroke-width="2.4" stroke-linecap="round" stroke-linejoin="round"/></svg>Stone cleaning</li>
  </ul>

  <div class="follow">
    <span class="follow-label">Follow US :</span>
    <span class="social-dot"></span>
    <span class="social-dot"></span>
    <span class="social-dot"></span>
    <span class="social-dot"></span>
    <svg class="mail-icon" viewBox="0 0 28 22"><rect x="1" y="2" width="26" height="18" fill="#ffffff"/><path d="M1 2 L14 12 L27 2" fill="none" stroke="#0f4c8a" stroke-width="2"/></svg>
  </div>

  <div class="brand-name">BRIGHTWALL</div>
  <div class="brand-tag">PAINTING AND DECORATING SERVICES</div>
  <div class="brand-rule left"></div>
  <div class="brand-dot"></div>
  <div class="brand-rule right"></div>

  <h1 class="headline">BRIGHTWALL</h1>
  <div class="headline-sub">PAINTING AND DECORATING</div>

  <div class="contact phone">
    <svg width="26" height="26" viewBox="0 0 24 24"><path d="M6.6 2.5 L9.5 6.2 L7.6 8.4 C8.7 11 10.9 13.3 13.6 14.5 L15.8 12.6 L19.5 15.4 L17.8 19.2 C11 19 5 13 4.8 6.2 Z" fill="none" stroke="#3f8fd8" stroke-width="2" stroke-linejoin="round"/></svg>
    <span class="value">07700 900 123</span>
  </div>
  <div class="contact email">
    <svg width="22" height="16" viewBox="0 0 22 16"><rect x="0" y="0" width="22" height="16" fill="#3f8fd8"/><path d="M0 0 L11 9 L22 0" fill="none" stroke="#ffffff" stroke-width="1.6"/></svg>
    <span class="value">info@brightwallpaintingdecorating.com</span>
  </div>
  <div class="contact web">
    <svg width="22" height="22" viewBox="0 0 22 22"><circle cx="11" cy="11" r="10" fill="#3f8fd8"/><g fill="none" stroke="#ffffff" stroke-width="1.2"><ellipse cx="11" cy="11" rx="4.5" ry="10"/><line x1="1" y1="11" x2="21" y2="11"/><line x1="3" y1="6" x2="19" y2="6"/><line x1="3" y1="16" x2="19" y2="16"/></g></svg>
    <span class="value">www.brightwallpaintingdecorating.com</span>
  </div>

  <div class="foot-bar"></div>
</main>
</body>
</html>
```